Mental Health care Company in Washington DC

We are a new mental health care services provider in Washington DC. Please look at these sites.
https://marlowbrookpartners.com
https://www.quillstoneinc.com
https://velmarsh-kt.org/
https://www.trivanqx.com
https://www.thelanternofqz.com

```html
<!DOCTYPE html>
<html lang="en">
<head>
<meta charset="utf-8">
<title>Velora Health Services</title>
<link rel="stylesheet" href="https://fonts.googleapis.com/css2?family=Poppins:wght@400;500;600;700&display=swap">
<style>
:root{
  --navy:#0b1f3f;
  --navy-deep:#0a1a38;
  --orange:#f5821f;
  --teal:#a3dbdc;
  --teal-soft:#c9ecec;
  --ink:#1c2230;
  --muted:#4b5563;
  --field:#f1f6f6;
  --white:#ffffff;
}
*{box-sizing:border-box;margin:0;padding:0}
html,body{width:1200px;height:4392px;overflow:hidden}
body{font-family:"Poppins",sans-serif;color:var(--ink);background:var(--white);position:relative}
.btn{position:absolute;display:flex;align-items:center;justify-content:center;background:var(--orange);color:var(--white);font-weight:600;font-size:14px;border-radius:24px}
h2.section-title{position:absolute;font-weight:600;font-size:36px;color:var(--navy);letter-spacing:.5px}
.center{left:0;width:1200px;text-align:center}

/* hero */
.hero{position:absolute;left:0;top:0;width:1200px;height:740px;overflow:hidden}
.hero-photo{position:absolute;inset:0;background:linear-gradient(100deg,#e7e4df 0%,#d8d3cd 35%,#9fb7d2 58%,#e8d2d3 80%,#d9d2cc 100%)}
.brand{position:absolute;left:61px;top:30px;font-weight:500;font-size:30px;color:var(--navy);line-height:1}
.brand small{display:block;font-size:10px;letter-spacing:6px;color:#5aa8ab;margin-top:4px;text-align:center;font-weight:400}
.nav{position:absolute;top:40px;left:327px;display:flex;gap:30px;font-size:13px;font-weight:500;color:var(--navy)}
.hero h1{position:absolute;left:61px;top:170px;font-weight:600;font-size:60px;line-height:88px;color:var(--navy);width:560px}
.hero p{position:absolute;left:61px;top:386px;width:470px;font-size:13px;line-height:23px;color:var(--ink)}

/* about */
.about-img{position:absolute;border-radius:14px;border:4px solid var(--white)}
.about p{position:absolute;left:516px;width:560px;font-size:13px;line-height:23px;color:var(--muted)}
.feature{position:absolute;top:1062px;display:flex;gap:12px;align-items:center}
.feature .ico{width:66px;height:66px;border-radius:50%;background:var(--teal);display:flex;align-items:center;justify-content:center}
.feature h3{font-weight:500;font-size:21px;color:var(--navy)}
.feature span{font-size:13px;color:var(--muted)}

/* services */
.service{position:absolute;top:1401px;width:350px;height:338px;border-radius:16px;background:var(--teal);padding:24px 12px 0 45px;color:var(--navy)}
.service::before{content:"";position:absolute;left:22px;top:24px;bottom:24px;width:3px;background:var(--navy)}
.service.featured{background:var(--navy);color:var(--white)}
.service.featured::before{background:var(--white)}
.service .ico{display:block;width:70px;height:70px;margin-left:5px}
.service h3{font-weight:500;font-size:21px;margin-top:24px;white-space:nowrap;letter-spacing:-.2px}
.service p{font-size:13px;line-height:25px;margin-top:22px;width:270px}
.read-more{position:absolute;left:45px;top:276px;display:inline-flex;align-items:center;gap:18px;padding:7px 14px 7px 26px;border-radius:20px;background:var(--navy);color:var(--white);font-size:13px}
.featured .read-more{background:var(--white);color:var(--navy)}

/* team */
.member{position:absolute;top:1994px;width:350px;height:700px}
.member .photo{position:absolute;top:143px;left:0;width:350px;height:352px;border-radius:24px;background:linear-gradient(180deg,#a3dbdc 0%,#8ccfd4 45%,#6fb3d6 100%)}
.member h3{position:absolute;top:512px;width:350px;text-align:center;font-weight:500;font-size:22px;color:var(--navy)}
.member .role{position:absolute;top:548px;width:350px;text-align:center;font-size:13px;color:var(--ink)}
.member p{position:absolute;top:578px;left:25px;width:300px;text-align:center;font-size:13px;line-height:24px;color:var(--muted)}
.member .social{position:absolute;top:660px;left:0;width:350px;display:flex;justify-content:center;gap:38px}
.dot{width:34px;height:34px;border-radius:50%;background:var(--ink)}

/* reviews */
.review{position:absolute;border-radius:12px;background:var(--teal);color:var(--navy);box-shadow:0 6px 14px rgba(0,0,0,.18)}
.review .avatar{position:absolute;border-radius:50%;background:radial-gradient(circle at 50% 40%,#d8a890,#5a3a2c);border:3px solid var(--white)}
.review .name{position:absolute;font-weight:600}
.review .q{position:absolute;font-size:36px;font-weight:700;color:#4a6670;line-height:1}
.review p{position:absolute;font-size:11px;line-height:21px}
.review.featured{background:var(--navy);color:var(--white)}
.review.featured .name{color:var(--teal)}
.review.featured .q{color:#7a8aa5}

/* contact */
.field-label{position:absolute;font-size:13px;font-weight:600;color:var(--navy)}
.field{position:absolute;height:58px;border-radius:18px;background:var(--field);box-shadow:0 3px 6px rgba(0,0,0,.12);font-size:13px;color:#6b7280;padding:18px 30px}
.info{position:absolute;left:757px;top:3418px;width:349px;height:446px;border-radius:12px;overflow:hidden;color:var(--white)}
.info .photo{position:absolute;inset:0;background:linear-gradient(160deg,#7f8ea8 0%,#5e7090 45%,#8c93a4 100%)}
.info .shade{position:absolute;inset:0;background:rgba(20,36,70,.55)}
.info h3{position:absolute;left:30px;top:32px;font-weight:600;font-size:22px}
.info .row{position:absolute;left:24px;display:flex;gap:12px;font-size:13px;line-height:20px}

/* footer */
.footer{position:absolute;left:0;top:3985px;width:1200px;height:407px;background:var(--navy-deep);color:var(--white)}
.footer .logo{position:absolute;left:0;width:1200px;top:62px;text-align:center;font-weight:500;font-size:62px;color:#7fc6c8;line-height:1}
.footer .logo small{display:block;font-size:20px;letter-spacing:14px;margin-top:8px;font-weight:400}
.footer nav{position:absolute;top:218px;left:0;width:1200px;display:flex;justify-content:center;font-size:13px}
.footer nav a{padding:0 38px;border-left:1px solid rgba(255,255,255,.6);color:var(--white);text-decoration:none}
.footer nav a:first-child{border-left:none}
.footer .social{position:absolute;top:286px;left:0;width:1200px;display:flex;justify-content:center;gap:40px}
.footer .social .dot{background:var(--white)}
.footer .rule{position:absolute;left:57px;top:353px;width:1083px;height:2px;background:rgba(255,255,255,.8)}
.footer .copy{position:absolute;left:57px;top:372px;font-size:13px}
.footer .legal{position:absolute;right:60px;top:372px;display:flex;gap:58px;font-size:13px}
</style>
</head>
<body>

<header class="hero">
  <div class="hero-photo" role="img" aria-label="Photo of a nurse gently helping an elderly woman walk in a bright room"></div>
  <div class="brand">Velora Health<small>SERVICES</small></div>
  <nav class="nav"><span>Home</span><span>About Us</span><span>Services</span><span>Meet Our Team</span><span>Reviews</span><span>Contact Us</span></nav>
  <div class="btn" style="left:973px;top:27px;width:168px;height:44px;">Booking Now</div>
  <h1>Helping You Heal, Grow And Thrive</h1>
  <p>massa et morbi. Sit arcu sodales dictum penatibus enim tincidunt quis. Mi nibh dictum neque eget malesuada facilisi dui dui Cursus est et adipiscing in. Nec nulla sit mauris varius senectus cras platea leo. Tempus mauris lobortis tellus ipsum</p>
  <div class="btn" style="left:61px;top:532px;width:166px;height:44px;">Booking Now</div>
</header>

<section class="about">
  <div class="about-img" style="left:61px;top:830px;width:282px;height:332px;background:linear-gradient(160deg,#d9d4cf,#8aa6c4);" role="img" aria-label="Photo of a caregiver supporting an elderly woman"></div>
  <div class="about-img" style="left:294px;top:858px;width:174px;height:164px;background:linear-gradient(160deg,#e6e1dc,#b7b1ab);" role="img" aria-label="Photo of a carer comforting an older man"></div>
  <div class="about-img" style="left:184px;top:950px;width:236px;height:272px;background:linear-gradient(160deg,#cfd1c8,#3f3a36);" role="img" aria-label="Photo of a nurse speaking with a senior man in a wheelchair"></div>
  <h2 class="section-title" style="left:516px;top:834px;">ABOUT US</h2>
  <p style="top:898px;">massa et morbi. Sit arcu sodales dictum penatibus enim tincidunt quis. Mi nibh dictum neque eget malesuada facilisi dui dui Cursus est et adipiscing in. Nec nulla sit mauris varius senectus cras platea leo. Tempus mauris lobortis tellus ipsum</p>
  <p style="top:978px;">massa et morbi. Sit arcu sodales dictum penatibus enim tincidunt quis. Mi nibh dictum neque eget malesuada facilisi est et adipiscing in.</p>
  <div class="feature" style="left:516px;">
    <div class="ico"><svg width="40" height="40" viewBox="0 0 40 40" fill="none" stroke="#0b1f3f" stroke-width="2"><circle cx="20" cy="20" r="16"/><circle cx="20" cy="20" r="10"/><circle cx="20" cy="20" r="4"/></svg></div>
    <div><h3>Our Mission</h3><span>Eget malesuada facilisi est et.</span></div>
  </div>
  <div class="feature" style="left:818px;">
    <div class="ico"><svg width="40" height="40" viewBox="0 0 40 40" fill="none" stroke="#0b1f3f" stroke-width="2"><circle cx="22" cy="14" r="9"/><path d="M22 9v10M17 14h10M4 30h8l8 4 14-6"/></svg></div>
    <div><h3>Our Value</h3><span>Eget malesuada facilisi iska.</span></div>
  </div>
  <div class="btn" style="left:516px;top:1176px;width:167px;height:44px;">Read More</div>
</section>

<section class="services">
  <h2 class="section-title center" style="top:1318px;">SERVICES</h2>
  <article class="service" style="left:61px;">
    <svg class="ico" viewBox="0 0 70 70" fill="none" stroke="#0b1f3f" stroke-width="2.5"><circle cx="35" cy="20" r="10"/><path d="M17 60V44c0-8 8-12 18-12s18 4 18 12v16"/></svg>
    <h3>Individual Therapy</h3>
    <p>Mi nibh dictum neque eget malesuada facilisi est et adipiscing in. Nec nulla sit mauris varius senectus cras platea leo.</p>
    <span class="read-more">Read More <svg width="12" height="16" viewBox="0 0 12 16" fill="none" stroke="currentColor" stroke-width="2.5"><path d="M3 2l6 6-6 6"/></svg></span>
  </article>
  <article class="service featured" style="left:424px;">
    <svg class="ico" viewBox="0 0 70 70" fill="none" stroke="#ffffff" stroke-width="2.5"><circle cx="35" cy="32" r="14"/><path d="M35 24v16M27 32h16M8 50c10 10 44 10 54 0"/></svg>
    <h3>Medication Management</h3>
    <p>Mi nibh dictum neque eget malesuada facilisi est et adipiscing in. Nec nulla sit mauris varius senectus cras platea leo.</p>
    <span class="read-more">Read More <svg width="12" height="16" viewBox="0 0 12 16" fill="none" stroke="currentColor" stroke-width="2.5"><path d="M3 2l6 6-6 6"/></svg></span>
  </article>
  <article class="service" style="left:789px;">
    <svg class="ico" viewBox="0 0 70 70" fill="none" stroke="#0b1f3f" stroke-width="2.5"><circle cx="32" cy="20" r="10"/><path d="M14 56c0-12 8-20 18-20"/><circle cx="48" cy="46" r="10"/><path d="M48 40v12M42 46h12"/></svg>
    <h3>Cognitive Health Support</h3>
    <p>Mi nibh dictum neque eget malesuada facilisi est et adipiscing in. Nec nulla sit mauris varius senectus cras platea leo.</p>
    <span class="read-more">Read More <svg width="12" height="16" viewBox="0 0 12 16" fill="none" stroke="currentColor" stroke-width="2.5"><path d="M3 2l6 6-6 6"/></svg></span>
  </article>
  <div class="btn" style="left:518px;top:1778px;width:167px;height:44px;">More Detail</div>
</section>

<section class="team">
  <h2 class="section-title center" style="top:1917px;left:25px;">MEET OUR TEAM</h2>
  <div class="member" style="left:61px;">
    <div class="photo" role="img" aria-label="Photo of a clinical psychologist in teal scrubs holding a clipboard"></div>
    <h3>Dr. Nadia Rowen</h3><div class="role">Clinical Psychologist</div>
    <p>Mi nibh dictum neque eget male suada Mi nibh dictum neque eget facilisi est et adipiscing in.</p>
    <div class="social"><span class="dot"></span><span class="dot"></span></div>
  </div>
  <div class="member" style="left:433px;">
    <div class="photo" role="img" aria-label="Photo of a clinical psychologist in blue scrubs with arms crossed"></div>
    <h3>Dr. Nadia Rowen</h3><div class="role">Clinical Psychologist</div>
    <p>Mi nibh dictum neque eget male suada Mi nibh dictum neque eget facilisi est et adipiscing in.</p>
    <div class="social"><span class="dot"></span><span class="dot"></span></div>
  </div>
  <div class="member" style="left:806px;">
    <div class="photo" role="img" aria-label="Photo of a clinical psychologist in blue scrubs with a stethoscope"></div>
    <h3>Dr. Nadia Rowen</h3><div class="role">Clinical Psychologist</div>
    <p>Mi nibh dictum neque eget male suada Mi nibh dictum neque eget facilisi est et adipiscing in.</p>
    <div class="social"><span class="dot"></span><span class="dot"></span></div>
  </div>
</section>

<section class="reviews">
  <h2 class="section-title center" style="top:2785px;">PATIENT REVIEWS</h2>
  <article class="review" style="left:61px;top:2915px;width:300px;height:196px;">
    <div class="avatar" role="img" aria-label="Reviewer portrait" style="left:10px;top:12px;width:62px;height:62px;"></div>
    <div class="name" style="left:80px;top:30px;font-size:16px;">Marisol</div>
    <div class="q" style="left:10px;top:100px;">&ldquo;</div>
    <p style="left:42px;top:96px;width:225px;">Ut arcu dictum sem placerat. Quis felis at sit in non vivamus nunc in habitant. Eget et massa et morbi. Sit arcu sodalesdictum sem placerat.</p>
    <div class="q" style="left:268px;top:160px;">&rdquo;</div>
  </article>
  <article class="review featured" style="left:395px;top:2879px;width:411px;height:266px;">
    <div class="avatar" role="img" aria-label="Reviewer portrait" style="left:12px;top:14px;width:86px;height:86px;"></div>
    <div class="name" style="left:108px;top:40px;font-size:22px;">Marisol</div>
    <div class="q" style="left:12px;top:136px;font-size:44px;">&ldquo;</div>
    <p style="left:57px;top:140px;width:310px;font-size:13px;line-height:24px;">Ut arcu dictum sem placerat. Quis felis at sit in non vivamus nunc in habitant. Eget et massa et morbi. Sit arcu sodalesdictum sem placerat.  Sit arcu sodalesdictum sem</p>
    <div class="q" style="left:370px;top:224px;font-size:44px;">&rdquo;</div>
  </article>
  <article class="review" style="left:842px;top:2915px;width:300px;height:196px;">
    <div class="avatar" role="img" aria-label="Reviewer portrait" style="left:10px;top:12px;width:62px;height:62px;"></div>
    <div class="name" style="left:80px;top:30px;font-size:16px;">Marisol</div>
    <div class="q" style="left:10px;top:100px;">&ldquo;</div>
    <p style="left:42px;top:96px;width:225px;">Ut arcu dictum sem placerat. Quis felis at sit in non vivamus nunc in habitant. Eget et massa et morbi. Sit arcu sodalesdictum sem placerat.</p>
    <div class="q" style="left:268px;top:160px;">&rdquo;</div>
  </article>
  <div class="btn" style="left:511px;top:3206px;width:167px;height:44px;">More Read</div>
</section>

<section class="contact">
  <h2 class="section-title" style="left:61px;top:3342px;">CONTACT US</h2>
  <div class="field-label" style="left:92px;top:3431px;">Full Name</div>
  <div class="field-label" style="left:422px;top:3431px;">Full Name</div>
  <div class="field" style="left:61px;top:3458px;width:314px;">Enter Your Full Name</div>
  <div class="field" style="left:390px;top:3458px;width:316px;">Enter Your Full Name</div>
  <div class="field-label" style="left:92px;top:3549px;">Full Name</div>
  <div class="field-label" style="left:422px;top:3549px;">Full Name</div>
  <div class="field" style="left:61px;top:3576px;width:314px;">Enter Your Full Name</div>
  <div class="field" style="left:390px;top:3576px;width:316px;">Enter Your Full Name</div>
  <div class="field-label" style="left:92px;top:3667px;">Full Name</div>
  <div class="field" style="left:61px;top:3694px;width:645px;height:128px;">Enter Your Full Name</div>
  <div class="btn" style="left:61px;top:3850px;width:167px;height:44px;">Submite Now</div>

  <aside class="info">
    <div class="photo" role="img" aria-label="Photo of a nurse shaking hands with an elderly man"></div>
    <div class="shade"></div>
    <h3>Information</h3>
    <div class="row" style="top:122px;">
      <svg width="28" height="28" viewBox="0 0 24 24" fill="#ffffff"><path d="M6.6 10.8a15 15 0 006.6 6.6l2.2-2.2c.3-.3.7-.4 1-.2 1.1.4 2.3.6 3.6.6.6 0 1 .4 1 1V20c0 .6-.4 1-1 1A17 17 0 013 4c0-.6.4-1 1-1h3.5c.6 0 1 .4 1 1 0 1.3.2 2.5.6 3.6.1.3 0 .7-.2 1z"/></svg>
      <div><b style="font-weight:500">Phone</b><br>014-862-509</div>
    </div>
    <div class="row" style="top:226px;">
      <svg width="30" height="28" viewBox="0 0 24 24" fill="#ffffff"><path d="M2 5h20v14H2z"/><path d="M2 5l10 8 10-8" fill="none" stroke="#5e7090" stroke-width="1.5"/></svg>
      <div><b style="font-weight:500">Email</b><br>hello@velorahealth.example</div>
    </div>
    <div class="row" style="top:332px;">
      <svg width="24" height="30" viewBox="0 0 24 30" fill="#ffffff"><path d="M12 0a10 10 0 00-10 10c0 8 10 20 10 20s10-12 10-20A10 10 0 0012 0zm0 14a4 4 0 110-8 4 4 0 010 8z"/></svg>
      <div><b style="font-weight:500">Address</b><br>18 Larkmoor Lane, Fenwick</div>
    </div>
  </aside>
</section>

<footer class="footer">
  <div class="logo">Velora Health<small>SERVICES</small></div>
  <nav><a>Home</a><a>About Us</a><a>Services</a><a>Meet Our Team</a><a>Reviews</a><a>Contact Us</a></nav>
  <div class="social"><span class="dot"></span><span class="dot"></span><span class="dot"></span><span class="dot"></span></div>
  <div class="rule"></div>
  <div class="copy">Copyright © 2025 All Right Reserved</div>
  <div class="legal"><span>Privacy Policy</span><span>Trems Of Service</span><span>Cooking Setting</span></div>
</footer>

</body>
</html>
```